larkwind flakies snack packaging

We are a new startup snack company that need a design for a snack packaging. Our snack goes by the name of larkwind flakies. Its a traditional snack usually eaten during festive seasons in south east asia region. The idea is to revolutionize the notion of the snack from one that is eaten during these celebratory seasons to an everyday one. The packaging design should be modern and minimalist yet fun too, also taking into consideration that it should not appear to be too childish. It should stand out from the other snacks products like potato chips etc if placed on the same shelf. The colour scheme is not decided yet as we are open to more ideas but colours should be complementary and not more than 2 or 3 hopefully. There should be also be an enthic sense of south east asian features on the design and it should reflects the Chinese, Malay and indian heritage. It need not be too obvious, a subtle kind should suffice. The packaging should also have the particular graphic/shape of the mould that i have upload followed by the picture of the snack. I have included a mock up of the logo of my company. Proposed designs can feel free to alter the larkwind graphic to a more modern, minimalist yet whimsical and fun. Proposed designs should have a front and back view of the packaging. We are looking to launch at 4 to 5 flavours like white sesame, black sesame, peanuts with white sesame and original.
Updates

Project Deadline Extended
Reason: Not enough submissions coming in yet.

Project Deadline Extended
Reason: Extension of deadline to allow more designs to come in.

Target Market(s)

All ages from as young as 5 to 6 years old to 60 to 70s.

Industry/Entity Type

It Company

Font styles to use
Other font styles liked:
• Fonts should be simple and minimalist. Easy for elderly to read without straining the eyes.

Requirements
Must have
• My logo which I have designed. Designers can feel free to tweak and enhance the design of the logo. The colour is not definite yet. Consumers must know what
• we are selling from the design of the packaging without guessing how it look
• like. The suggested packaging dimension is 17cm (W) by 23.5cm (H).
Nice to have
• We are looking to print the package using kraft paper which I have attached.
Should not have
• religious inclination of motifs, logo etc.

```html
<!DOCTYPE html>
<html lang="en">
<head>
<meta charset="utf-8">
<title>larkwind flakies – pouch range</title>
<link rel="stylesheet" href="https://fonts.googleapis.com/css2?family=Ubuntu:wght@400;500&family=Open+Sans:wght@600&display=swap">
<style>
  :root {
    --backdrop: #6b6b6b;
    --kraft: #dcc39d;
    --kraft-light: #e6d0ad;
    --kraft-shade: #c9ad85;
    --ink-dark: #2b2118;
    --flavour-green: #0f6a55;
    --flavour-orange: #d7742a;
    --flavour-brown: #a97c4f;
    --flavour-magenta: #a11a60;
    --white: #ffffff;
  }
  * { box-sizing: border-box; margin: 0; padding: 0; }
  html, body { width: 1200px; height: 1000px; overflow: hidden; }
  body {
    background: var(--backdrop);
    font-family: "Ubuntu", sans-serif;
  }
  .range {
    position: absolute;
    top: 262px;
    left: 55px;
    width: 1090px;
    display: flex;
    justify-content: space-between;
  }
  .pouch {
    position: relative;
    width: 262px;
    height: 474px;
    background: linear-gradient(180deg, var(--kraft-light) 0%, var(--kraft) 45%, var(--kraft) 100%);
    border-radius: 10px 10px 18px 18px;
  }
  .pouch__seal {
    position: absolute;
    top: 36px; left: 0; right: 0;
    height: 8px;
    border-top: 1px solid var(--kraft-shade);
    border-bottom: 1px solid var(--kraft-shade);
    opacity: .8;
  }
  .brand-mark {
    position: absolute;
    top: 84px; left: 0; right: 0;
    display: flex; justify-content: center; align-items: center; gap: 5px;
    font-size: 13px; font-weight: 500;
    color: var(--accent);
  }
  .brand-mark__dot {
    width: 10px; height: 10px; border-radius: 50%;
    background: var(--accent);
  }
  .flavour-label {
    position: absolute;
    top: 126px; left: 50%;
    transform: translateX(-50%);
    width: 206px; height: 106px;
    background: var(--accent);
    color: var(--label-ink, var(--white));
    display: flex; flex-direction: column; justify-content: center; align-items: center;
    text-align: center;
  }
  .flavour-label__name { font-size: 21px; font-weight: 400; line-height: 1.1; }
  .flavour-label__flavour { font-size: 14px; line-height: 1.15; margin-top: 4px; }
  .native-name {
    position: absolute;
    top: 256px; left: 50%;
    transform: translateX(-50%);
    width: 170px; height: 176px;
    border-radius: 6px;
    background: radial-gradient(ellipse at center, var(--accent) 0%, transparent 75%);
    opacity: .28;
  }
  .net-weight {
    position: absolute;
    bottom: 14px; left: 0; right: 0;
    text-align: center;
    font-family: "Open Sans", sans-serif;
    font-weight: 600;
    font-size: 10px;
    color: var(--ink-dark);
  }
  .pouch--white-sesame { --accent: var(--flavour-green); }
  .pouch--original { --accent: var(--flavour-orange); --label-ink: var(--ink-dark); }
  .pouch--peanut-sesame { --accent: var(--flavour-brown); --label-ink: var(--ink-dark); }
  .pouch--black-sesame { --accent: var(--flavour-magenta); }
</style>
</head>
<body>
  <main class="range">
    <article class="pouch pouch--white-sesame">
      <div class="pouch__seal"></div>
      <div class="brand-mark"><span class="brand-mark__dot"></span>larkwind</div>
      <div class="flavour-label">
        <span class="flavour-label__name">larkwind flakies</span>
        <span class="flavour-label__flavour">white sesame</span>
      </div>
      <div class="native-name" role="img" aria-label="Large faint brush-lettered product name in Chinese"></div>
      <p class="net-weight">Net Weight 70grams</p>
    </article>
    <article class="pouch pouch--original">
      <div class="pouch__seal"></div>
      <div class="brand-mark"><span class="brand-mark__dot"></span>larkwind</div>
      <div class="flavour-label">
        <span class="flavour-label__name">larkwind flakies</span>
        <span class="flavour-label__flavour">original</span>
      </div>
      <div class="native-name" role="img" aria-label="Large faint brush-lettered product name in Chinese"></div>
      <p class="net-weight">Net Weight 70grams</p>
    </article>
    <article class="pouch pouch--peanut-sesame">
      <div class="pouch__seal"></div>
      <div class="brand-mark"><span class="brand-mark__dot"></span>larkwind</div>
      <div class="flavour-label">
        <span class="flavour-label__name">larkwind flakies</span>
        <span class="flavour-label__flavour">peanuts with<br>white sesame</span>
      </div>
      <div class="native-name" role="img" aria-label="Large faint brush-lettered product name in Chinese"></div>
      <p class="net-weight">Net Weight 70grams</p>
    </article>
    <article class="pouch pouch--black-sesame">
      <div class="pouch__seal"></div>
      <div class="brand-mark"><span class="brand-mark__dot"></span>larkwind</div>
      <div class="flavour-label">
        <span class="flavour-label__name">larkwind flakies</span>
        <span class="flavour-label__flavour">black sesame</span>
      </div>
      <div class="native-name" role="img" aria-label="Large faint brush-lettered product name in Chinese"></div>
      <p class="net-weight">Net Weight 70grams</p>
    </article>
  </main>
</body>
</html>
```